Upscale business cards needed for Board of Directors

We need professional business cards created for members of our family business Board of Directors. We would like these relatively simple and straightforward, but also with a unique element to set them apart. Probably stick with neutral and simple colors - white, grey etc. We need space for the traditional elements, including name, title, address, email/phone number. And we will be creating several from this template so it needs to be template that is easy to switch information in and out of.
Business
See description

```html
<!DOCTYPE html>
<html lang="en">
<head>
<meta charset="utf-8">
<title>Keelstone Holdings – Business Card</title>
<link href="https://fonts.googleapis.com/css2?family=Lato:wght@400;700&family=Cinzel:wght@500&family=Courier+Prime&display=swap" rel="stylesheet">
<style>
  :root {
    --backdrop: #e9e9e7;
    --card: #ffffff;
    --ink: #1f1f1f;
    --ink-soft: #555555;
    --accent-tan: #b3a68a;
    --band-grey: #8e8e8e;
    --band-text: #ffffff;
  }
  html, body {
    margin: 0;
    padding: 0;
    width: 1200px;
    height: 799px;
    overflow: hidden;
    background: var(--backdrop);
  }
  .card {
    position: absolute;
    left: 150px;
    top: 142px;
    width: 900px;
    height: 514px;
    background: var(--card);
    box-shadow: 0 8px 28px rgba(0,0,0,0.14);
    overflow: hidden;
  }
  .accent-rule {
    position: absolute;
    left: 28px;
    top: 38px;
    width: 560px;
    height: 6px;
    background: var(--accent-tan);
  }
  .company-name {
    position: absolute;
    left: 28px;
    top: 58px;
    margin: 0;
    font-family: "Lato", sans-serif;
    font-weight: 700;
    font-size: 58px;
    letter-spacing: 2px;
    line-height: 1;
    color: var(--ink);
    text-transform: uppercase;
  }
  .person {
    position: absolute;
    left: 28px;
    top: 190px;
  }
  .person-name {
    margin: 0;
    font-family: "Cinzel", serif;
    font-weight: 500;
    font-size: 34px;
    color: var(--ink);
    line-height: 1.1;
  }
  .person-title {
    margin: 2px 0 0;
    font-family: "Courier Prime", monospace;
    font-size: 22px;
    letter-spacing: 2px;
    color: var(--ink-soft);
  }
  .contact-band {
    position: absolute;
    left: 0;
    bottom: 0;
    width: 100%;
    height: 196px;
    background: var(--band-grey);
    color: var(--band-text);
    font-family: "Lato", sans-serif;
    font-size: 25px;
    box-sizing: border-box;
    padding: 38px 28px 0;
  }
  .contact-line {
    margin: 0 0 26px;
    white-space: nowrap;
  }
  .sep {
    padding: 0 12px;
  }
</style>
</head>
<body>
  <article class="card">
    <div class="accent-rule"></div>
    <h1 class="company-name">Keelstone Holdings</h1>

    <div class="person">
      <p class="person-name">Name Surname</p>
      <p class="person-title">Designation</p>
    </div>

    <footer class="contact-band">
      <p class="contact-line">118B W. Cedar Bend Rd. Lakemont, TX. 75310<span class="sep">|</span>(512) 555 - 0143</p>
      <p class="contact-line">www.KeelstoneGroup.co<span class="sep">|</span>Morgan@KeelstoneGroup.co</p>
    </footer>
  </article>
</body>
</html>
```